Commercial Web Site for software product

Ledgerly is a GDPR compliant Membership, Contact Management & List Management solution. It is an ideal replacement for any organisation or company still using Sheetwise, Postbox Mail, simple database or paper-based system to manage contact data, mail lists, and other personal information.
The target market will be Clubs/Associations in the EU.
The design will need to be a fluid design and suitable for mobile devices. The home page will contain most of the web site content, enabling a user to scroll through all the relevant information on one page. There will be a single sub page design required for supporting information.
The web site will need to support two language versions - English and German (Language selection option required). However, the build requirements will be for a static HTML site (no database) in English only. We will duplicate and make the German version ourselves.
The attached document is the first draft of the home page content. Whilst it is a little wordy, it should convey the main information that we wish to get across.
Please note: We would prefer not to use photographs for the main imagery, we feel vector graphics would be a better option . As a guide, the following design: https://en.pixelvane.example/profiles/Marlowe/designs/5502147 may provide an insight into how we imagine the home page working and contains all the key elements we would expect to be covered.
The logo contained in the attached document can be split into a logo and text. Feel free to use only the logo (without text) or separate and place the text alongside etc., We do not want to change the logo, however, how you chose to use it is up to you.
Colour's are also optional. We like the blue, but are open to alternative ideas.
The testimonials section, should contain all the questions (3) and several of the associated answers shown. Questions/Answers may be separated into speech bubbles or similar. Not all answers will be used, but are there to provide some content.
The sub pages will be used to provide background on the GDPR requirements, our Service Offering, About Us (possibly), and a contact page.
Updates
The design budget is now guaranteed.
Whilst we have no intention not to move forward with this project, I understand the 'lack of commitment' from our side may be a negative.
Once we have reviewed all submissions - we will decide upon our preferred submission.
We will only request changes from one or two designers, and will make it clear how many other designers are in the running. This I believe is fair, as you probably need this information before deciding whether to submit any changes requested!
My hope is we have a home page that enables a visitor to clearly understand what we are offering, without having to drill down into various sub pages or sections to understand the basics. I appreciate we need to write appropriate content, but the design itself should feel uncluttered and fluid.
Hopefully some of you really talented designers can throw some ideas into the pot. The concept is more important than the detail.
Thanks for considering this project.
Coding
Number of Pages Required
Font styles to use
Colors
Look and feel

```html
<!DOCTYPE html>
<html lang="en">
<head>
<meta charset="utf-8">
<title>Ledgerly – Coordinate all your membership &amp; contact data</title>
<link rel="stylesheet" href="https://fonts.googleapis.com/css2?family=Nunito:wght@400;600;700;800&display=swap">
<style>
:root{
  --blue:#2e7fe3;
  --blue-deep:#1c5fc4;
  --blue-soft:#dcebfd;
  --blue-pale:#eef5fe;
  --navy:#17264a;
  --ink:#2b3550;
  --muted:#6b7690;
  --white:#ffffff;
  --line:#d7e3f3;
}
*{box-sizing:border-box;margin:0;padding:0}
html,body{width:1200px;height:5352px;overflow:hidden}
body{font-family:"Nunito",sans-serif;color:var(--ink);background:var(--white);position:relative}
.section{position:absolute;left:0;width:1200px}
.btn{display:inline-block;border-radius:22px;font-weight:700;font-size:15px;padding:11px 24px;text-decoration:none}
.btn-white{background:var(--white);color:var(--blue-deep);box-shadow:0 6px 16px rgba(20,60,130,.25)}
.art{position:absolute;border-radius:24px}
h2.title{font-size:44px;font-weight:400;color:var(--navy);line-height:1.1}
h2.title b{font-weight:800}

/* hero */
.hero{top:0;height:760px;background:linear-gradient(160deg,#5aa6f3 0%,#2f7de1 55%,#1f66cc 100%)}
.nav{position:absolute;top:18px;left:36px;right:40px;display:flex;align-items:center}
.brand{font-size:28px;font-weight:700;color:var(--white)}
.nav-links{margin-left:auto;display:flex;gap:22px;align-items:center;font-size:15px;font-weight:600;color:var(--white)}
.nav-links .pill{padding:7px 18px;border-radius:18px;background:var(--white);color:var(--blue-deep)}
.nav-links .pill-dark{padding:7px 18px;border-radius:18px;background:var(--navy);color:var(--white)}
.hero h1{position:absolute;top:140px;left:70px;width:500px;font-size:50px;line-height:1.08;font-weight:800;color:var(--white)}
.hero p{position:absolute;top:380px;left:70px;width:490px;font-size:16px;line-height:1.5;color:var(--white)}
.hero .btn{position:absolute;top:480px;left:70px}
.hero-art{left:600px;top:80px;width:560px;height:530px;background:radial-gradient(circle at 50% 50%,#f6f9ff 0%,#b9d6f8 45%,rgba(46,127,227,0) 72%)}
.wave{position:absolute;left:0;width:1200px}

/* streamlined */
.streamlined{top:760px;height:420px}
.streamlined h2{position:absolute;left:70px;top:10px}
.cards{position:absolute;left:70px;top:140px;display:flex;gap:40px}
.card{width:320px;height:200px;background:var(--white);border-radius:14px;box-shadow:0 8px 28px rgba(30,70,140,.14);text-align:center;padding:20px 34px}
.card svg{width:36px;height:36px}
.card h3{font-size:19px;font-weight:800;color:var(--navy);margin:8px 0 6px}
.card p{font-size:13px;line-height:1.4;color:var(--muted)}

/* functionality */
.functionality{top:1180px;height:1200px;background:linear-gradient(180deg,#fff 0%,var(--blue-pale) 45%,#fff 100%)}
.functionality h2{position:absolute;top:55px;width:100%;text-align:center}
.feature h3{font-size:40px;font-weight:400;color:var(--navy);margin-bottom:20px}
.ticks{list-style:none;font-size:15px;line-height:1.2}
.ticks li{display:flex;gap:10px;margin-bottom:11px;color:var(--ink);font-weight:600}
.ticks li svg{flex:none;width:18px;height:18px}
.ticks .sub{list-style:none;margin:-4px 0 10px 28px;font-size:14px;line-height:1.5;color:var(--ink)}
.ticks .sub li{display:list-item;margin:0;font-weight:400}
.ticks .sub li::before{content:"• ";color:var(--blue)}
.feature-a{position:absolute;left:70px;top:140px;width:480px}
.feature-b{position:absolute;left:640px;top:640px;width:480px}

/* easy */
.easy{top:2380px;height:730px}
.easy h2{text-align:center;padding-top:10px}
.easy .intro{width:1080px;margin:24px auto 0;font-size:17px;line-height:1.5;color:var(--ink)}
.steps{position:absolute;left:70px;top:220px;width:560px;list-style:none}
.steps li{display:flex;gap:26px;margin-bottom:34px;font-size:16px;line-height:1.5}
.steps .num{font-size:44px;font-weight:700;color:var(--blue-deep);line-height:1;width:30px}
.steps b{font-weight:800}

/* stored */
.stored{top:3110px;height:540px;background:linear-gradient(180deg,#dbeafc 0%,#c8defa 100%)}
.stored h2{position:absolute;left:70px;top:120px}
.stored p{position:absolute;left:70px;top:200px;width:640px;font-size:14px;line-height:1.65;color:var(--ink)}
.stored .btn{position:absolute;left:70px;top:440px}

/* testimonials */
.testimonials{top:3650px;height:730px}
.testimonials h2{text-align:center;padding-top:50px}
.testimonials .lead{width:1080px;margin:26px auto 0;text-align:center;font-size:17px;line-height:1.5}
.testimonials .lead-strong{text-align:center;font-weight:800;font-size:16px;margin-top:14px}
.carousel{position:absolute;left:0;top:280px;width:1200px;height:330px}
.bubble{position:absolute;border-radius:18px;padding:26px 30px;font-size:22px;line-height:1.35}
.bubble-q{left:130px;top:20px;width:460px;height:210px;background:var(--blue);color:var(--white);box-shadow:0 10px 28px rgba(30,90,180,.3)}
.bubble-a{background:var(--white);color:var(--blue-deep);box-shadow:0 8px 24px rgba(30,70,140,.14);width:350px;font-size:20px}
.arrow{position:absolute;top:90px;width:40px;height:40px;border-radius:50%;background:var(--white);box-shadow:0 4px 14px rgba(30,70,140,.2)}
.dots{position:absolute;top:360px;left:560px;display:flex;gap:14px}
.dots span{width:18px;height:18px;border-radius:50%;border:3px solid var(--blue)}
.dots span.on{background:var(--blue)}

/* cta */
.cta{top:4380px;height:640px;background:linear-gradient(170deg,#4d9cf0 0%,#2f7de1 60%,#216bd2 100%)}
.try{position:absolute;left:70px;top:130px;width:500px;color:var(--white)}
.try .pill-title{display:inline-block;background:var(--white);color:var(--navy);font-size:38px;font-weight:700;padding:12px 36px;border-radius:40px}
.try p{margin-top:30px;font-size:14px;line-height:1.6}
.try .login{margin-top:22px;font-size:14px;line-height:1.5}
.try .login b{font-weight:800}
.form{position:absolute;left:620px;top:70px;width:510px;color:var(--white)}
.form h3{font-size:36px;font-weight:400}
.form .note{font-size:14px;margin:10px 0 16px;line-height:1.45}
.field label{display:block;font-size:14px;margin-bottom:4px}
.field .box{height:34px;background:var(--white);border-radius:3px;margin-bottom:14px}
.field .box.tall{height:120px}

/* footer */
.footer{top:5020px;height:332px;background:linear-gradient(180deg,#fff 0%,#eaf3fd 100%)}
.footer .brand{position:absolute;left:70px;top:90px;color:var(--navy);font-size:24px}
.footer .copy{position:absolute;left:70px;top:130px;font-size:12px;line-height:1.5;color:var(--muted)}
.socials{position:absolute;left:70px;top:180px;display:flex;gap:10px}
.socials span{width:26px;height:26px;border-radius:50%;background:var(--blue-deep)}
.fcol{position:absolute;top:92px;font-size:13px;color:var(--ink);line-height:1.9}
.fcol h4{font-size:12px;letter-spacing:3px;color:var(--muted);font-weight:700;margin-bottom:6px}
</style>
</head>
<body>

<header class="section hero">
  <nav class="nav">
    <div class="brand">ledgerly</div>
    <div class="nav-links">
      <span>About</span>
      <span class="pill">Login</span>
      <span class="pill-dark">Get started for free</span>
    </div>
  </nav>
  <h1>Coordinate all your membership &amp; contact data</h1>
  <p>Ledgerly is the fast, secure, GDPR compliant solution for managing and coordinating all your Membership and Contact data, and generating GDPR compliant Marketing lists.</p>
  <a class="btn btn-white" href="#">Try it now</a>
  <div class="art hero-art" role="img" aria-label="Illustration of a contact card being filed into a secure blue database"></div>
  <svg class="wave" style="top:590px" height="170" viewBox="0 0 1200 170" preserveAspectRatio="none">
    <path d="M0 110 C260 40 520 150 800 90 C980 50 1100 60 1200 20 L1200 170 L0 170Z" fill="#cfe3fb" opacity=".7"/>
    <path d="M0 140 C300 80 560 170 860 120 C1020 95 1120 90 1200 70 L1200 170 L0 170Z" fill="#ffffff"/>
  </svg>
</header>

<section class="section streamlined">
  <h2 class="title">Streamlined<br><b>data management</b></h2>
  <div class="cards">
    <div class="card">
      <svg viewBox="0 0 24 24"><path d="M2 11 22 3 17 21 11 14Z" fill="#2e7fe3"/><path d="M11 14 22 3" stroke="#fff" stroke-width="1.4"/></svg>
      <h3>Paperless</h3>
      <p>Ideal replacement for any organisation or company still using Sheetwise, Postbox Mail, simple database or paper-based system to manage contact data, mail lists and other personal information.</p>
    </div>
    <div class="card">
      <svg viewBox="0 0 24 24"><path d="M12 2 20 5v7c0 5-3.5 8.5-8 10-4.5-1.5-8-5-8-10V5Z" fill="#2e7fe3"/><rect x="9" y="10.5" width="6" height="5" rx="1" fill="#fff"/><path d="M10 10.5V9a2 2 0 0 1 4 0v1.5" stroke="#fff" stroke-width="1.4" fill="none"/></svg>
      <h3>GDPR Compliant</h3>
      <p>It is a GDPR compliant Membership, Contact Management &amp; List Management solution.</p>
    </div>
    <div class="card">
      <svg viewBox="0 0 24 24"><rect x="3" y="4" width="18" height="16" rx="2" fill="#2e7fe3"/><path d="M7 9h10M7 13h10M7 17h6" stroke="#fff" stroke-width="1.6"/></svg>
      <h3>Marketing lists</h3>
      <p>Coordinating all your Membership and Contact data, and generating GDPR compliant Marketing lists.</p>
    </div>
  </div>
</section>

<section class="section functionality">
  <h2 class="title"><b>Functionality</b> of ledgerly</h2>

  <div class="feature feature-a">
    <h3>Securely Manage</h3>
    <ul class="ticks">
      <li><svg viewBox="0 0 18 18"><circle cx="9" cy="9" r="9" fill="#2e7fe3"/><path d="M5 9.5 8 12l5-6" stroke="#fff" stroke-width="2" fill="none"/></svg>Attendance registration &amp; management</li>
      <li><svg viewBox="0 0 18 18"><circle cx="9" cy="9" r="9" fill="#2e7fe3"/><path d="M5 9.5 8 12l5-6" stroke="#fff" stroke-width="2" fill="none"/></svg>Time recording</li>
      <li><svg viewBox="0 0 18 18"><circle cx="9" cy="9" r="9" fill="#2e7fe3"/><path d="M5 9.5 8 12l5-6" stroke="#fff" stroke-width="2" fill="none"/></svg>Relationship management</li>
      <li><svg viewBox="0 0 18 18"><circle cx="9" cy="9" r="9" fill="#2e7fe3"/><path d="M5 9.5 8 12l5-6" stroke="#fff" stroke-width="2" fill="none"/></svg>Donation Management</li>
      <li><svg viewBox="0 0 18 18"><circle cx="9" cy="9" r="9" fill="#2e7fe3"/><path d="M5 9.5 8 12l5-6" stroke="#fff" stroke-width="2" fill="none"/></svg>Prospect Management</li>
      <li><svg viewBox="0 0 18 18"><circle cx="9" cy="9" r="9" fill="#2e7fe3"/><path d="M5 9.5 8 12l5-6" stroke="#fff" stroke-width="2" fill="none"/></svg>Full Opt-In preferences management</li>
      <li><svg viewBox="0 0 18 18"><circle cx="9" cy="9" r="9" fill="#2e7fe3"/><path d="M5 9.5 8 12l5-6" stroke="#fff" stroke-width="2" fill="none"/></svg>Centralised secure permission-based access</li>
      <li><svg viewBox="0 0 18 18"><circle cx="9" cy="9" r="9" fill="#2e7fe3"/><path d="M5 9.5 8 12l5-6" stroke="#fff" stroke-width="2" fill="none"/></svg>GDPR compliant storage of all contact data</li>
      <li style="display:block"><ul class="sub"><li>Members</li><li>E-Mail addresses</li><li>Mobile &amp; Telephone numbers</li><li>Social Media</li></ul></li>
    </ul>
  </div>
  <div class="art" style="left:620px;top:170px;width:520px;height:290px;background:linear-gradient(135deg,#c9def9,#5c9ef0)" role="img" aria-label="Illustration of a secure dashboard with data panels and a padlock"></div>

  <div class="art" style="left:60px;top:600px;width:520px;height:400px;background:linear-gradient(135deg,#e4effd,#7fb2f2)" role="img" aria-label="Illustration of a laptop, tablet and phone showing the application"></div>
  <div class="feature feature-b">
    <h3>Everything, everywhere</h3>
    <ul class="ticks">
      <li><svg viewBox="0 0 18 18"><circle cx="9" cy="9" r="9" fill="#2e7fe3"/><path d="M5 9.5 8 12l5-6" stroke="#fff" stroke-width="2" fill="none"/></svg>Tasks/To-Do's</li>
      <li><svg viewBox="0 0 18 18"><circle cx="9" cy="9" r="9" fill="#2e7fe3"/><path d="M5 9.5 8 12l5-6" stroke="#fff" stroke-width="2" fill="none"/></svg>Document storage</li>
      <li><svg viewBox="0 0 18 18"><circle cx="9" cy="9" r="9" fill="#2e7fe3"/><path d="M5 9.5 8 12l5-6" stroke="#fff" stroke-width="2" fill="none"/></svg>Notes/history</li>
      <li><svg viewBox="0 0 18 18"><circle cx="9" cy="9" r="9" fill="#2e7fe3"/><path d="M5 9.5 8 12l5-6" stroke="#fff" stroke-width="2" fill="none"/></svg>Access using any device (PC, Laptop, Mobile, Tablet etc.)</li>
      <li><svg viewBox="0 0 18 18"><circle cx="9" cy="9" r="9" fill="#2e7fe3"/><path d="M5 9.5 8 12l5-6" stroke="#fff" stroke-width="2" fill="none"/></svg>Profiling tools for targeted GDPR compliant list generation</li>
      <li><svg viewBox="0 0 18 18"><circle cx="9" cy="9" r="9" fill="#2e7fe3"/><path d="M5 9.5 8 12l5-6" stroke="#fff" stroke-width="2" fill="none"/></svg>Avoid duplication of data and easily generate personalised GDPR compliant marketing lists for all contact data</li>
      <li style="display:block"><ul class="sub"><li>E-Mail addresses</li><li>Telephone numbers</li><li>Mobile numbers</li><li>Social Media addresses</li><li>Postal addresses</li></ul></li>
    </ul>
  </div>
</section>

<section class="section easy">
  <h2 class="title">ledgerly makes it <b>easy</b></h2>
  <p class="intro">One of the biggest challenges faced from most organisations when moving from a manual record keeping system (Sheetwise, Postbox Mail, simple database, or paper etc.) is how to manage, and coordinate all the various silos of information, to arrive at a single, valid <b>‘source of truth’</b>.</p>
  <ol class="steps">
    <li><span class="num">1</span><span>Paper records, typically need to be entered manually, however, <b>these records can also be organised to minimise duplication</b>. We advise clients to enter this data themselves, as a practical training exercise to familiarise their team with how the system works and establish confidence. <b>This Master Data can be cleaned and categorised</b> to show Opt-In preferences and areas of interest to assist with profiling/segmentation for future Mail lists.</span></li>
    <li><span class="num">2</span><span>The Master Data will be <b>returned for approval</b>.</span></li>
    <li><span class="num">3</span><span>Once agreed, the Master Data will be imported for you with the necessary access permissions assigned <b>ready</b> for you to start using the system from day one.</span></li>
  </ol>
  <div class="art" style="left:700px;top:230px;width:430px;height:470px;background:linear-gradient(160deg,#eef5fe,#9cc3f5)" role="img" aria-label="Illustration of stacked paper records being converted into digital contact cards"></div>
</section>

<section class="section stored">
  <svg class="wave" style="top:0" height="90" viewBox="0 0 1200 90" preserveAspectRatio="none"><path d="M0 0H1200V30C900 90 500 10 0 70Z" fill="#ffffff"/></svg>
  <h2 class="title">Where is the <b>data stored</b></h2>
  <p>We provide a fully hosted service within an ISO certified European Data Centre. This can be accessed 24 hours a day, from anywhere you have Internet access. Our service provides all the necessary technologies, a managed server platform, SQL database server and SSL certificates etc. to ensure you can start using the system without requiring additional technical support to set up and configure your own server. The systems are automatically maintained to ensure all important service patches and security updates are applied, and protected by firewall. Clients that wish to use their own infrastructure can do so. However, they will be responsible for the supply, installation and on-going maintenance of all infrastructure. We will of course fully support the Ledgerly software.</p>
  <a class="btn btn-white" href="#">Start now</a>
  <div class="art" style="left:800px;top:40px;width:300px;height:460px;background:linear-gradient(180deg,#f3f7fe,#8ab6f1)" role="img" aria-label="Illustration of a secure server rack"></div>
  <svg class="wave" style="bottom:0" height="90" viewBox="0 0 1200 90" preserveAspectRatio="none"><path d="M0 60C400 0 800 100 1200 30V90H0Z" fill="#ffffff"/></svg>
</section>

<section class="section testimonials">
  <h2 class="title">Client <b>Testimonials</b></h2>
  <p class="lead">Clients working with manual systems quickly see how <b>Ledgerly helps them establish a centralised source of truth</b>, greatly reducing the effort required to find information, and avoid the duplication – so often encountered with manual Sheetwise/Postbox Mail and paper-based processes.</p>
  <p class="lead-strong">This is what our clients said to our questions about Ledgerly.</p>
  <div class="carousel">
    <span class="arrow" style="left:30px"><svg viewBox="0 0 40 40" width="40" height="40"><path d="M23 13 16 20l7 7" stroke="#2e7fe3" stroke-width="3" fill="none"/></svg></span>
    <div class="bubble bubble-q">What is the main benefit/output of the program for you? (Which functions make your work easier and why?)</div>
    <div class="bubble bubble-a" style="left:700px;top:20px">Attendance list on tablet - simple overview of present children</div>
    <div class="bubble bubble-a" style="left:700px;top:170px">Note function - easy and fast</div>
    <span class="arrow" style="left:1130px"><svg viewBox="0 0 40 40" width="40" height="40"><path d="M17 13l7 7-7 7" stroke="#2e7fe3" stroke-width="3" fill="none"/></svg></span>
    <div class="dots"><span class="on"></span><span></span><span></span></div>
  </div>
</section>

<section class="section cta">
  <svg class="wave" style="top:-1px" height="80" viewBox="0 0 1200 80" preserveAspectRatio="none"><path d="M0 0H1200V10C850 80 400 0 0 50Z" fill="#ffffff"/></svg>
  <div class="try">
    <span class="pill-title">Try ledgerly now</span>
    <p>Click the button to <b>explore Ledgerly</b> yourself. This link provides Read-Only access to a test system. This access should provide an insight into how you could manage your contact data in an efficient, productive, and GDPR compliant manner. Cookie Statement here.</p>
    <p class="login"><b>Login details</b><br>User: demo<br>Password: ReadOnlyAccess</p>
  </div>
  <div class="form">
    <h3>Arrange A Presentation</h3>
    <p class="note">To arrange a software presentation or request further information – please use the contact form.</p>
    <div class="field"><label>Your Name (required)</label><div class="box"></div></div>
    <div class="field"><label>Your Email (required)</label><div class="box"></div></div>
    <div class="field"><label>Subject</label><div class="box"></div></div>
    <div class="field"><label>Your Message</label><div class="box tall"></div></div>
  </div>
  <svg class="wave" style="bottom:-1px" height="90" viewBox="0 0 1200 90" preserveAspectRatio="none"><path d="M0 70C350 10 800 100 1200 40V90H0Z" fill="#ffffff"/></svg>
</section>

<footer class="section footer">
  <div class="brand">Ledgerly</div>
  <p class="copy">Copyright © 2019 Ledgerly.<br>All Rights Reserved.</p>
  <div class="socials"><span></span><span></span><span></span><span></span></div>
  <div class="fcol" style="left:550px"><h4>PRODUCT</h4>About</div>
  <div class="fcol" style="left:970px"><h4>COMPANY</h4>Terms of Service<br>Privacy Policy</div>
</footer>

</body>
</html>
```